Brightmere Business Card Redesign & Logo Update

We need to update our business cards to something more modern and fresh. Brightmere can provide the current color schemes and old design examples, but welcome creativity in helping us with this redesign. PLEASE NOTE that we no longer utilize the "tree" and/or "leaf" imagery in our branding. If able would apprecaite an update on the quality of our "words only" logo in Ai. / PNG formats too.

Target Market(s)

Investors, landowners, corporate partners, contractors

Industry/Entity Type

Environmental Restoration & Conservation

Contact Information for Business Card

Logo, persons name, title, mailing address, phone and email, website url

Font styles to use
Other font styles liked:
• Merriweather

Requirements
Nice to have
• Logo, persons name, title, mailing address, phone and email, website url, but open to ideams
Should not have
• No all back backgrounds

```html
<!DOCTYPE html>
<html lang="en">
<head>
<meta charset="utf-8">
<title>Brightmere Business Card</title>
<link rel="stylesheet" href="https://fonts.googleapis.com/css2?family=Merriweather:wght@400;700;900&display=swap">
<style>
  :root{
    --stage:#dfe2e5;
    --card:#ffffff;
    --green:#068332;
    --forest:#24392a;
    --ink:#1d1d1d;
    --icon-grey:#6f6f73;
    --white:#ffffff;
  }
  *{margin:0;padding:0;box-sizing:border-box}
  html,body{width:1200px;height:780px;overflow:hidden;background:var(--stage)}
  body{font-family:"Merriweather",Georgia,serif;color:var(--ink)}
  .stage{position:relative;width:1200px;height:780px}
  .card{position:absolute;width:540px;height:310px;background:var(--card);border-radius:22px;overflow:hidden;box-shadow:0 10px 28px rgba(0,0,0,.18)}
  .card--front{left:40px;top:235px}
  .card--back{left:620px;top:235px}
  .card__shapes{position:absolute;inset:0;width:100%;height:100%}
  .wordmark{position:absolute;line-height:1}
  .wordmark__name{display:block;font-weight:900;color:var(--green);letter-spacing:.5px}
  .wordmark__tagline{display:block;font-weight:700;color:var(--ink);text-transform:uppercase;letter-spacing:1.2px;margin-top:8px}
  .card--front .wordmark{left:190px;top:95px}
  .card--front .wordmark__name{font-size:44px}
  .card--front .wordmark__tagline{font-size:12.5px}
  .card--back .wordmark{left:40px;top:42px}
  .card--back .wordmark__name{font-size:30px}
  .card--back .wordmark__tagline{font-size:9px;margin-top:6px}
  .front-web{position:absolute;left:58px;top:266px;display:flex;align-items:center;gap:8px;color:var(--white);font-size:13px;line-height:1;white-space:nowrap}
  .contact{position:absolute;left:262px;top:128px;width:260px}
  .contact__row{display:flex;align-items:flex-start;gap:12px;margin-bottom:12px}
  .contact__icon{flex:none;width:28px;height:28px;border-radius:50%;display:flex;align-items:center;justify-content:center}
  .contact__icon--dark{background:var(--forest)}
  .contact__icon--grey{background:var(--icon-grey)}
  .contact__text{font-size:10.5px;line-height:1.45}
  .contact__name{font-size:15px;font-weight:700;letter-spacing:.8px;text-transform:uppercase;line-height:1.1}
  .contact__title{font-size:9px;letter-spacing:1.2px;text-transform:uppercase;margin-top:3px}
</style>
</head>
<body>
<main class="stage">

  <section class="card card--front" aria-label="Business card front">
    <svg class="card__shapes" viewBox="0 0 540 310" aria-hidden="true">
      <polygon points="0,84 70,84 100,92 0,94" fill="var(--forest)"/>
      <polygon points="0,92 100,92 145,220 540,272 540,310 0,310" fill="var(--green)"/>
      <polygon points="145,220 470,310 20,310 0,296 0,250" fill="var(--forest)"/>
    </svg>
    <div class="wordmark">
      <span class="wordmark__name">BRIGHTMERE</span>
      <span class="wordmark__tagline">Environmental Credit Company</span>
    </div>
    <div class="front-web">
      <svg width="14" height="14" viewBox="0 0 14 14" aria-hidden="true"><g fill="none" stroke="var(--white)" stroke-width="1.2"><circle cx="7" cy="7" r="6"/><ellipse cx="7" cy="7" rx="2.6" ry="6"/><line x1="1" y1="7" x2="13" y2="7"/></g></svg>
      <span>www.brightmerecredit.com</span>
    </div>
  </section>

  <section class="card card--back" aria-label="Business card back">
    <svg class="card__shapes" viewBox="0 0 540 310" aria-hidden="true">
      <polygon points="0,124 70,124 110,130 0,132" fill="var(--forest)"/>
      <polygon points="0,130 112,130 250,310 0,310" fill="var(--green)"/>
    </svg>
    <div class="wordmark">
      <span class="wordmark__name">BRIGHTMERE</span>
      <span class="wordmark__tagline">Environmental Credit Company</span>
    </div>
    <div class="contact">
      <div class="contact__row">
        <span class="contact__icon contact__icon--dark">
          <svg width="14" height="14" viewBox="0 0 14 14" aria-hidden="true"><circle cx="7" cy="4.5" r="2.8" fill="var(--white)"/><path d="M2 13c0-3 2.3-5 5-5s5 2 5 5z" fill="var(--white)"/></svg>
        </span>
        <div>
          <div class="contact__name">Henry Calloway</div>
          <div class="contact__title">Founder</div>
        </div>
      </div>
      <div class="contact__row">
        <span class="contact__icon contact__icon--grey">
          <svg width="14" height="14" viewBox="0 0 14 14" aria-hidden="true"><path d="M3 1.5l2.2 2.8-1.3 1.5c.8 1.6 2.1 2.9 3.7 3.7l1.5-1.3 2.8 2.2-1.3 2C6.2 12.2 1.8 7.8 1 2.8z" fill="var(--white)"/></svg>
        </span>
        <div class="contact__text">+000 55501 2468<br>+000 55501 2468</div>
      </div>
      <div class="contact__row">
        <span class="contact__icon contact__icon--grey">
          <svg width="14" height="14" viewBox="0 0 14 14" aria-hidden="true"><g fill="none" stroke="var(--white)" stroke-width="1.2"><circle cx="7" cy="7" r="6"/><ellipse cx="7" cy="7" rx="2.6" ry="6"/><line x1="1" y1="7" x2="13" y2="7"/></g></svg>
        </span>
        <div class="contact__text">www.brightmerecredit.com<br>hello@brightmerecredit.com</div>
      </div>
      <div class="contact__row">
        <span class="contact__icon contact__icon--dark">
          <svg width="14" height="14" viewBox="0 0 14 14" aria-hidden="true"><path d="M7 13S2.5 8.2 2.5 5.3a4.5 4.5 0 0 1 9 0C11.5 8.2 7 13 7 13z" fill="var(--white)"/><circle cx="7" cy="5.3" r="1.7" fill="var(--forest)"/></svg>
        </span>
        <div class="contact__text">48 Fernhollow Lane,<br>Ashvale</div>
      </div>
    </div>
  </section>

</main>
</body>
</html>
```